website design for online company - registration of companies AUSTRALIA

website name: velmora482.com.au
purpose of the website: register NEW australian companies

once a client submits their order, our website will submit information to a government agency and in under 20 minutes, the client will receive their new company together with legal documentation:

key features:
- simplicity
- ease of use
- clarity
- fast
- competitive
- trust

our competitors:
www.quickdratel.com.au
www.zentrafirms.com.au

the website needs to be dynamic, clear and portray simplicity as the name suggests.

"register your company online with OREV in 3 simple steps"
1 fill in a short form
2 submit payment
3 receive your company

headings - similar to our competitors but needs to be different.

Design only no coding

if you have any questions, feel free to ask

people in business

Government

Serif

• simple
creative
elegant
• top graphics

```html
<!DOCTYPE html>
<html lang="en">
<head>
<meta charset="utf-8">
<title>velmora482.com.au – website design</title>
<link rel="stylesheet" href="https://fonts.googleapis.com/css2?family=Arimo:wght@400;700&display=swap">
<style>
:root{
  --board:#474747;
  --panel:#e3e3e3;
  --navy:#0d2a5c;
  --blue:#0a56c8;
  --blue-deep:#0a3d94;
  --ink:#222;
  --grey-text:#555;
  --steps-bg:#ececec;
  --footer-dark:#2b2b2b;
  --white:#fff;
}
*{box-sizing:border-box;margin:0;padding:0}
html,body{width:1200px;height:927px;overflow:hidden}
body{background:var(--board);font-family:"Arimo",Arial,sans-serif;color:var(--ink);position:relative}

.presentation-panel{position:absolute;background:var(--panel)}
.panel-home{left:29px;top:130px;width:545px;height:484px}
.panel-about{left:627px;top:130px;width:546px;height:420px}

.page{position:absolute;background:var(--white);box-shadow:0 0 6px rgba(0,0,0,.55);overflow:hidden}
.page-home{left:136px;top:142px;width:331px;height:458px}
.page-about{left:736px;top:142px;width:329px;height:396px}

.phone-tab{position:absolute;right:0;top:0;width:74px;height:11px;background:linear-gradient(90deg,#1e6ad6,var(--blue-deep));
  clip-path:polygon(8px 0,100% 0,100% 100%,0 100%);color:var(--white);font-size:6.5px;font-weight:700;line-height:11px;padding-left:22px}
.phone-tab svg{position:absolute;left:13px;top:2px}

.site-logo{position:absolute;left:15px;top:19px;font-size:10.5px;font-weight:700;color:var(--navy);letter-spacing:-.1px}
.site-logo span{color:var(--blue)}
.main-nav{position:absolute;top:21px;display:flex;gap:5px;font-size:4.2px;color:#444;letter-spacing:.2px}
.main-nav a{color:inherit;text-decoration:none;padding:1.5px 3px;border-radius:1px}
.main-nav a.active{background:var(--blue);color:var(--white);font-weight:700}
.page-home .main-nav{left:150px}
.page-about .main-nav{left:143px}
.header-rule{position:absolute;left:0;right:0;top:32px;height:1px;background:#d8d8d8}

/* hero */
.hero{position:absolute;left:0;top:33px;width:331px;height:117px;overflow:hidden;
  background:radial-gradient(ellipse 150px 45px at 110px 95px,rgba(120,190,255,.45),transparent 70%),
  linear-gradient(180deg,#1b6ee0 0%,var(--blue) 45%,var(--blue-deep) 100%)}
.hero-title{position:absolute;left:18px;top:18px;color:var(--white);font-size:11px;font-weight:700}
.hero-sub{position:absolute;left:18px;top:31px;color:var(--white);font-size:5.3px;line-height:5.6px}
.btn-register{position:absolute;left:58px;top:84px;width:87px;height:17px;border-radius:2px;
  background:linear-gradient(#fafafa,#c9c9c9);border:1px solid #8a8a8a;color:var(--blue-deep);font-size:6.5px;
  line-height:15px;padding-left:8px}
.btn-register i{position:absolute;right:0;top:0;width:17px;height:15px;background:#444;border-radius:0 2px 2px 0}
.btn-register svg{position:absolute;right:5px;top:4.5px}
.hero-photo{position:absolute;left:178px;top:0;width:135px;height:117px;
  background:linear-gradient(100deg,rgba(255,255,255,0) 0%,rgba(225,232,242,.55) 35%,rgba(200,210,225,.45) 65%,rgba(40,60,100,.35) 100%)}

/* steps */
.steps{position:absolute;left:0;top:150px;width:331px;height:49px;background:var(--steps-bg);border-bottom:1px solid #ddd}
.steps h2{position:absolute;left:21px;top:6px;font-size:5.3px;font-weight:700;color:#333}
.step{position:absolute;top:18px;display:flex;gap:5px;font-size:3.9px;color:#666;line-height:4.4px}
.step b{display:block;color:#333;font-weight:400;font-size:4.6px}
.step-icon{width:19px;height:20px;border-radius:1px}
.step-1{left:23px}.step-1 .step-icon{background:linear-gradient(#c8955a,#8a5b2c)}
.step-2{left:123px}.step-2 .step-icon{background:linear-gradient(#e69a3a,#9a5a16)}
.step-3{left:234px}.step-3 .step-icon{background:linear-gradient(#f2b73f,#c57f12)}
.step-divider{position:absolute;top:16px;width:1px;height:24px;background:#cdcdcd}

/* columns */
.feature{position:absolute;top:207px;width:91px}
.feature h3{font-size:8.5px;font-weight:700;color:#333;margin-bottom:4px}
.feature-photo{width:91px;height:49px;background:linear-gradient(135deg,#dfe6ee,#6b7f97 60%,#2c3a4e)}
.feature p{font-size:3.9px;line-height:4.7px;color:var(--grey-text);margin-top:6px}
.btn-more{display:inline-block;margin-top:6px;font-size:3.6px;color:#444;border:1px solid #bbb;background:#f3f3f3;padding:1.5px 5px}
.link-list{list-style:none;margin-top:3px;font-size:4px;color:var(--blue)}
.link-list li{border-top:1px solid #ccc;padding:2px 0 2px 7px;position:relative}
.link-list li::before{content:"";position:absolute;left:1px;top:3px;border:1.6px solid transparent;border-left:2.4px solid #333}

/* footer */
.footer{position:absolute;left:0;width:100%;background:linear-gradient(180deg,#1769d5,#0c4aa7 60%,#0a3e8c);color:var(--white)}
.footer h4{font-size:5px;font-weight:700;margin-bottom:7px}
.footer-col{position:absolute;top:7px;font-size:3.9px;line-height:4.9px}
.footer-col ul{list-style:none}
.footer-col p{margin-bottom:3px}
.footer-bar{position:absolute;left:0;width:100%;background:var(--footer-dark);color:#ddd;font-size:3.6px}
.social{position:absolute;left:14px;top:6px;display:flex;gap:5px}
.social i{width:5px;height:5px;background:#4e8fd8;border-radius:1px}
.copyright{position:absolute;right:14px;top:6px}

/* about page */
.page-title-bar{position:absolute;left:0;top:33px;width:100%;height:29px;
  background:radial-gradient(ellipse 140px 20px at 220px 28px,rgba(120,190,255,.45),transparent 70%),linear-gradient(180deg,#1b6ee0,var(--blue-deep))}
.page-title-bar h1{position:absolute;left:14px;top:10px;font-size:7.5px;color:var(--white);font-weight:700}
.about-copy{position:absolute;left:14px;top:74px;width:212px;font-size:3.9px;line-height:5px;color:var(--grey-text)}
.about-copy p{margin-bottom:8px}
.sidebar{position:absolute;left:240px;top:62px;width:89px;height:241px;background:#f4f4f4;box-shadow:-2px 0 4px rgba(0,0,0,.15)}
.sidebar h4{margin:0 6px;padding:3px 0 3px 2px;font-size:4.5px;background:linear-gradient(90deg,#ddd,#f4f4f4);color:#222}
.side-nav{list-style:none;margin:3px 6px 14px;font-size:3.9px;color:var(--blue)}
.side-nav li{padding:2px 0 2px 9px;border-bottom:1px solid #ccc;position:relative}
.side-nav li::before{content:"";position:absolute;left:3px;top:3px;border:1.5px solid transparent;border-left:2.3px solid var(--blue)}
.client-box{display:block;margin:4px 0 5px 9px;width:57px;height:23px;background:#c9c9c9;border:1px solid #b4b4b4;
  color:var(--blue-deep);font-size:6.5px;font-weight:700;line-height:21px;text-align:center}
</style>
</head>
<body>

<div class="presentation-panel panel-home"></div>
<div class="presentation-panel panel-about"></div>

<section class="page page-home">
  <div class="phone-tab"><svg width="6" height="6" viewBox="0 0 10 10"><path d="M2 0l2 2-1 2 3 3 2-1 2 2-2 2C4 10 0 6 0 2z" fill="#fff"/></svg>140-555-0182</div>
  <div class="site-logo">VELMORA<span>482</span>.COM.AU</div>
  <nav class="main-nav"><a class="active">HOME</a><a>ABOUT</a><a>SERVICES</a><a>REGISTER COMPANY</a><a>CONTACT US</a></nav>
  <div class="header-rule"></div>

  <div class="hero">
    <div class="hero-photo" role="img" aria-label="Businessman standing in front of a large wall clock"></div>
    <div class="hero-title">VELMORA482.COM.AU</div>
    <p class="hero-sub">submit information to a government agency<br>under 20 minutes,<br>you will receive your new company together<br>with legal documentation</p>
    <div class="btn-register">REGISTER NOW<i><svg width="7" height="6" viewBox="0 0 7 6"><path d="M0 2h4V0l3 3-3 3V4H0z" fill="#fff"/></svg></i></div>
  </div>

  <div class="steps">
    <h2>Register Your Company Online with OREV in 3 Simple Steps</h2>
    <div class="step step-1"><div class="step-icon" role="img" aria-label="Clipboard with form"></div><div><b>fill in a short form</b>Lorem ipsum dolor sit amet,<br>consectetur adipiscing elit.</div></div>
    <div class="step-divider" style="left:114px"></div>
    <div class="step step-2"><div class="step-icon" role="img" aria-label="Wallet for payment"></div><div><b>submit payment</b>Lorem ipsum dolor sit amet,<br>consectetur adipiscing elit.</div></div>
    <div class="step-divider" style="left:225px"></div>
    <div class="step step-3"><div class="step-icon" role="img" aria-label="Company documents folder"></div><div><b>receive your company</b>Lorem ipsum dolor sit amet,<br>consectetur adipiscing elit.</div></div>
  </div>

  <article class="feature" style="left:16px">
    <h3>ABOUT US?</h3>
    <div class="feature-photo" role="img" aria-label="Group of business people in suits"></div>
    <p>Lorem ipsum dolor sit amet, consectetur adipiscing elit. Etiam tristique tristique lacus in varius. Donec nec vestibulum ligula. Aenean turpis diam, feugiat a luctus in, rhoncus eget risus. Maecenas consequat porttitor dui, vitae consequat massa imperdiet ut. Ut tempus lobortis, eros leo molestie velit, non egestas augue nulla eget nisl.</p>
    <span class="btn-more">READ MORE</span>
  </article>
  <article class="feature" style="left:120px">
    <h3>WHY HIRE US?</h3>
    <div class="feature-photo" role="img" aria-label="Business people working at a laptop"></div>
    <p>Lorem ipsum dolor sit amet, consectetur adipiscing elit. Etiam tristique tristique lacus in varius. Donec nec vestibulum ligula. Aenean turpis diam, feugiat a luctus in, rhoncus eget risus. Maecenas consequat porttitor dui, vitae consequat massa imperdiet ut. Donec laoreet, elit ut tempus lobortis, eros leo molestie velit, non egestas augue nulla eget nisl.</p>
    <span class="btn-more">READ MORE</span>
  </article>
  <article class="feature" style="left:225px">
    <h3>WHAT YOU GET?</h3>
    <div class="feature-photo" role="img" aria-label="Business handshake across a desk"></div>
    <p>Lorem ipsum dolor sit amet, consectetur adipiscing elit. Etiam tristique tristique lacus in varius. Donec nec vestibulum ligula. Aenean turpis diam, feugiat a luctus in, rhoncus eget risus. Maecenas consequat porttitor dui, vitae consequat massa imperdiet ut.</p>
    <ul class="link-list"><li>Website Design</li><li>Blog Design</li><li>Branding design</li></ul>
  </article>

  <footer class="footer" style="top:365px;height:71px">
    <div class="footer-col" style="left:14px"><h4>Browse Site</h4>
      <ul><li>About our company</li><li>Contact us</li><li>Our Portfolio</li><li>Our Prices</li><li>Online quote form</li><li>Client Testimonials</li></ul></div>
    <div class="footer-col" style="left:84px;width:98px"><h4>Our Testimonials</h4>
      <p>Lorem ipsum dolor sit amet, consectetur adipiscing elit. Etiam tristique tristique lacus in varius. Donec nec vestibulum ligula. Aenean turpis diam, feugiat a luctus in, rhoncus eget risus. Maecenas consequat porttitor dui, vitae consequat massa imperdiet ut. elit ut tempus lobortis, eros leo molestie velit.</p><b>John Doe, Anonymous</b></div>
    <div class="footer-col" style="left:211px;width:98px"><h4>From Our Blog</h4>
      <p>April 25, 2014<br><b>Lorem ipsum dolor sit amet, consectetur</b> adipiscing elit. Etiam tristique lacus in varius. Donec nec vestibulum ligula.</p>
      <p>April 20, 2014<br><b>Lorem ipsum dolor sit amet, consectetur</b> adipiscing elit. Etiam tristique lacus in varius. Donec nec vestibulum ligula.</p></div>
  </footer>
  <div class="footer-bar" style="top:436px;height:22px"><div class="social"><i></i><i></i><i></i></div><span class="copyright">Copyright © 2014. All rights reserved.</span></div>
</section>

<section class="page page-about">
  <div class="phone-tab"><svg width="6" height="6" viewBox="0 0 10 10"><path d="M2 0l2 2-1 2 3 3 2-1 2 2-2 2C4 10 0 6 0 2z" fill="#fff"/></svg>140-555-0182</div>
  <div class="site-logo">VELMORA<span>482</span>.COM.AU</div>
  <nav class="main-nav"><a>HOME</a><a class="active">ABOUT</a><a>SERVICES</a><a>REGISTER COMPANY</a><a>CONTACT US</a></nav>
  <div class="header-rule"></div>
  <div class="page-title-bar"><h1>About Us</h1></div>

  <div class="about-copy">
    <p>Lorem ipsum dolor sit amet, consectetur adipiscing elit. Donec viverra porta ullamcorper. Fusce a purus arcu, id congue quam. Sed urna felis, aliquet eu iaculis ac, aliquet vitae arcu. Integer id cursus magna. Vestibulum pulvinar dolor id magna vulputate at sagittis lectus luctus. Aenean pretium commodo lobortis. Proin ac augue enim, ut pulvinar ligula. In auctor egestas sem id tempor. Fusce iaculis vehicula orci. Nam rutrum ante in nisl facilisis eget placerat diam ullamcorper. Donec tincidunt magna at ligula tincidunt eget fringilla odio tincidunt. Ut pharetra nulla a nisl consectetur rutrum. Aenean eros mauris, posuere sit amet luctus eu, rhoncus ut arcu.</p>
    <p>Cras pharetra nulla sapien eget pretium. Fusce id velit nisl. In eleifend, nibh in auctor malesuada, sem magna interdum diam, et tincidunt sem orci vel justo. Vestibulum nec sapien velit. Aenean ultrices dapibus mi, et dignissim eros mattis in. Aliquam eget dignissim purus. Sed sed nisi sed nisl feugiat imperdiet. Nam elementum velit sed neque mollis gravida. Proin eget ligula dolor.</p>
    <p>Cras viverra, magna quis facilisis cursus, nulla urna posuere orci, ac gravida quam mi nec massa. Nam dapibus euismod lacus, in accumsan lectus pretium sed. Suspendisse mollis nulla in mauris luctus euismod ullamcorper arcu egestas. Nulla facilisi. Cras ac sapien nisi, placerat pellentesque enim. Nunc condimentum ligula ac odio feugiat vitae egestas sem aliquet. Nulla feugiat dui vel tellus consequat porttitor rutrum magna varius. Proin ut urna felis, in adipiscing nisl. In libero metus, pharetra eget molestie ut, dignissim eget mi.</p>
    <p>Nam vulputate nisl at libero porttitor venenatis. Quisque quam tortor, euismod nec lobortis sed, lobortis sodales augue. Pellentesque accumsan convallis eleifend. Suspendisse eu est diam, vitae tempor magna. Suspendisse at neque convallis neque sagittis ultrices. Fusce dapibus posuere elit quis vestibulum. Morbi in consectetur massa. Nunc tempor, est a fermentum tempus, odio orci congue eros, non mollis est eros eget dolor. Ut eleifend viverra nunc, in lobortis libero lacinia sit amet. Vestibulum tristique porta nulla et dapibus. Duis ut tortor arcu. Vestibulum scelerisque dapibus eros at sagittis. Cum sociis natoque penatibus et magnis dis parturient montes, nascetur ridiculus mus. Sed sit amet dolor odio. In nunc mi, porta eu facilisis at, ullamcorper at enim.</p>
  </div>

  <aside class="sidebar">
    <div style="height:11px"></div>
    <h4>Side Navigation</h4>
    <ul class="side-nav"><li>Who we are</li><li>What we do</li><li>Testimonials</li><li>Employment</li></ul>
    <h4>Our Clients</h4>
    <div style="height:4px"></div>
    <span class="client-box">CLIENT LOGO</span>
    <span class="client-box">CLIENT LOGO</span>
    <span class="client-box">CLIENT LOGO</span>
    <span class="client-box">CLIENT LOGO</span>
  </aside>

  <footer class="footer" style="top:303px;height:74px">
    <div class="footer-col" style="left:14px"><h4>Browse Site</h4>
      <ul><li>About our company</li><li>Contact us</li><li>Our Portfolio</li><li>Our Prices</li><li>Online quote form</li><li>Client Testimonials</li></ul></div>
    <div class="footer-col" style="left:84px;width:98px"><h4>Our Testimonials</h4>
      <p>Lorem ipsum dolor sit amet, consectetur adipiscing elit. Etiam tristique tristique lacus in varius. Donec nec vestibulum ligula. Aenean turpis diam, feugiat a luctus in, rhoncus eget risus. Maecenas consequat porttitor dui, vitae consequat massa imperdiet ut. elit ut tempus lobortis, eros leo molestie velit.</p><b>John Doe, Anonymous</b></div>
    <div class="footer-col" style="left:209px;width:100px"><h4>From Our Blog</h4>
      <p>April 25, 2014<br><b>Lorem ipsum dolor sit amet, consectetur</b> adipiscing elit. Etiam tristique lacus in varius. Donec nec vestibulum ligula.</p>
      <p>April 20, 2014<br><b>Lorem ipsum dolor sit amet, consectetur</b> adipiscing elit. Etiam tristique lacus in varius. Donec nec vestibulum ligula.</p></div>
  </footer>
  <div class="footer-bar" style="top:377px;height:19px"><div class="social"><i></i><i></i><i></i></div><span class="copyright">Copyright © 2014. All rights reserved.</span></div>
</section>

</body>
</html>
```